Q-Rolls Business Card

We are a modern retail clothing store. Established in 1994. I need a presentable card that will amaze vendors when given to them.

Front: Logo in middle
Info Side:

Name: Tomas Velder
Cell: 630-812-4463
Work: 630-917-3384 EXT. 417
Email: Tomas@q-rolls-example.com
Website: www.Q-rolls-example.com

Industry/Entity Type

Business

```html
<!DOCTYPE html>
<html lang="en">
<head>
<meta charset="utf-8">
<title>Q-Rolls Business Card</title>
<link rel="stylesheet" href="https://fonts.googleapis.com/css2?family=Arimo:wght@400;700&family=Michroma&display=swap">
<style>
  :root {
    --navy-deep: #121c30;
    --gap-white: #ffffff;
    --logo-black: #070908;
    --logo-frame: #5a6272;
    --back-blue-light: #2d4a80;
    --back-blue-dark: #1a3260;
    --panel-top: #131c33;
    --panel-body: #1c2b5e;
    --ink-white: #ffffff;
  }
  * { margin: 0; padding: 0; box-sizing: border-box; }
  html, body {
    width: 939px; height: 1200px; overflow: hidden;
    background: var(--gap-white);
  }
  .canvas { position: relative; width: 939px; height: 1200px; }

  .card-front {
    position: absolute; left: 0; top: 0; width: 939px; height: 563px;
    background: var(--navy-deep);
  }
  .logo-plate {
    position: absolute; left: 220px; top: 185px; width: 500px; height: 190px;
    background: var(--logo-black);
    border: 5px solid var(--logo-frame);
    display: flex; align-items: center; justify-content: center;
  }
  .logo-name {
    font-family: "Michroma", sans-serif;
    font-size: 56px; color: var(--ink-white);
    letter-spacing: 1px;
  }

  .card-back {
    position: absolute; left: 0; top: 603px; width: 939px; height: 597px;
    background: radial-gradient(ellipse at 30% 40%, var(--back-blue-light), var(--back-blue-dark) 80%);
  }
  .apparel-icons {
    position: absolute; left: 73px; top: 186px; width: 342px; height: 218px;
    background: linear-gradient(180deg, rgba(255,255,255,0.55), rgba(255,255,255,0.4));
    border-radius: 8px;
  }
  .contact-panel {
    position: absolute; left: 475px; top: 15px; width: 423px; height: 576px;
    background: var(--panel-body);
  }
  .name-block {
    height: 206px; background: var(--panel-top);
    padding: 88px 0 0 30px;
  }
  .person-name {
    font-family: "Arimo", sans-serif; font-weight: 700;
    font-size: 31px; color: var(--ink-white);
  }
  .contact-row {
    position: absolute; left: 26px; display: flex; align-items: center;
    font-family: "Arimo", sans-serif; font-size: 22.5px; line-height: 29px;
    color: var(--ink-white);
  }
  .contact-row svg { width: 34px; height: 34px; flex: none; margin-right: 28px; }
  .row-phone { top: 268px; }
  .row-web { top: 345px; }
</style>
</head>
<body>
<div class="canvas">
  <section class="card-front">
    <div class="logo-plate"><span class="logo-name">Q-Rolls</span></div>
  </section>

  <section class="card-back">
    <div class="apparel-icons" role="img" aria-label="Set of white apparel icons: dress, jacket, handbag, bikini, t-shirt and belt"></div>

    <div class="contact-panel">
      <div class="name-block"><h1 class="person-name">Tomas Velder</h1></div>

      <div class="contact-row row-phone">
        <svg viewBox="0 0 24 24" aria-hidden="true"><path fill="#fff" d="M6.6 10.8c1.4 2.8 3.8 5.1 6.6 6.6l2.2-2.2c.3-.3.7-.4 1-.2 1.1.4 2.3.6 3.6.6.6 0 1 .4 1 1V20c0 .6-.4 1-1 1C10.6 21 3 13.4 3 4c0-.6.4-1 1-1h3.5c.6 0 1 .4 1 1 0 1.3.2 2.5.6 3.6.1.3 0 .7-.2 1z"/></svg>
        <div>Cell: 630-812-4463<br>Work: 630-917-3384 EXT. 417</div>
      </div>

      <div class="contact-row row-web">
        <svg viewBox="0 0 24 24" aria-hidden="true" fill="none" stroke="#fff" stroke-width="1.6"><circle cx="12" cy="12" r="10"/><ellipse cx="12" cy="12" rx="4.5" ry="10"/><path d="M2 12h20M4 6.5h16M4 17.5h16"/></svg>
        <div>Tomas@q-rolls-example.com<br>www.Q-rolls-example.com</div>
      </div>
    </div>
  </section>
</div>
</body>
</html>
```